Stationary for New Company

We need stationary designed for a new company. Details of the required stationary is attached.

The final version should be trendy, clean... only 2 colours (green + grey/black) and professional.

#1: Business Cards (design on 2 sides)
#2: Letterhead (word format)
#3: Cover Page and back cover for proposals
#4: Envelopes,
#5: Thank You card,
#6: Presentation Folder,
#7: Email signatures template (sample attached in word document)

Logo is attached. Logo can be reversed out (will attach once available). Logo can be stacked or horizontal (provided as horizontal).

Files need to be provided in ai + png format.

Target Market(s)

Business owners. More affluent.

Industry/Entity Type

Business

Requirements
Must have
• See brief

Font: Calibri
Should not have
• Photographs / stock photos

```html
<!DOCTYPE html>
<html lang="en">
<head>
<meta charset="utf-8">
<title>Larkfield Insurance Brokers – Presentation Folder</title>
<link href="https://fonts.googleapis.com/css2?family=Carlito:wght@400&display=swap" rel="stylesheet">
<style>
  :root {
    --backdrop: #dedede;
    --paper: #f4f4f4;
    --brand-green: #6a8f45;
    --brand-green-dark: #5e8139;
  }
  * { margin: 0; padding: 0; box-sizing: border-box; }
  html, body {
    width: 1200px;
    height: 1000px;
    overflow: hidden;
    background: var(--backdrop);
  }
  .canvas {
    position: relative;
    width: 1200px;
    height: 1000px;
  }
  .folder-cover {
    position: absolute;
    left: 290px;
    top: 62px;
    width: 620px;
    height: 877px;
    background: var(--paper);
    box-shadow: 0 6px 18px rgba(0, 0, 0, 0.18);
    overflow: hidden;
  }
  .folder-wave {
    position: absolute;
    inset: 0;
    width: 100%;
    height: 100%;
  }
  .folder-wave path { fill: var(--brand-green); }
  .brand-lockup {
    position: absolute;
    top: 58px;
    right: 66px;
    width: 200px;
    display: flex;
    flex-direction: column;
    align-items: center;
    font-family: "Carlito", "Calibri", sans-serif;
    font-weight: 400;
    color: var(--brand-green);
    text-align: center;
  }
  .brand-square {
    width: 46px;
    height: 46px;
    background: var(--brand-green);
    margin-bottom: 10px;
  }
  .brand-name {
    font-size: 38px;
    line-height: 1;
    letter-spacing: 0.5px;
  }
  .brand-descriptor {
    font-size: 16px;
    line-height: 1.2;
    letter-spacing: 0.4px;
  }
</style>
</head>
<body>
  <main class="canvas">
    <section class="folder-cover" aria-label="Presentation folder front cover">
      <svg class="folder-wave" viewBox="0 0 620 877" preserveAspectRatio="none" aria-hidden="true">
        <path d="M0,26 C60,160 130,205 250,195 C380,185 480,220 560,250 C600,268 615,300 620,324 L620,877 L0,877 Z"/>
      </svg>
      <div class="brand-lockup">
        <span class="brand-square" aria-hidden="true"></span>
        <span class="brand-name">Larkfield</span>
        <span class="brand-descriptor">Insurance Brokers</span>
      </div>
    </section>
  </main>
</body>
</html>
```